Etiketten für Gin
Zielgruppe
Wir organisieren Alpaka-Events, Wanderungen, Geburtstage, Dating-Veranstaltungen und vertreiben Alpaka Produkte. Unser Gutshof befindet sich direkt an einem Schloss. Unsere Zielgruppe ist jede*r von 1-99 Jahren.
Aufgabenstellung
Das Etikett ist für unseren eigenen Gin. Es sollte unbedingt edel und hochwertig sein, so wie die regionalen Zutaten unseres Gins. Nicht zu farbenfroh-eher einfärbig, edel mit goldenen Elementen. Der Gin heißt Brunnwieser Hof Gin. Im Mittelpunkt sollte das Schloss stehen. Elemente wie Wälder, Teiche und Alpakas können in kleinen, feinen Details vorkommen.

```html
<!DOCTYPE html>
<html lang="de">
<head>
<meta charset="utf-8">
<title>Brunnwieser Hof Gin – Etikett</title>
<link rel="stylesheet" href="https://fonts.googleapis.com/css2?family=Playfair+Display:wght@400;900&display=swap">
<style>
  :root {
    --paper: #efefee;
    --label: #f7f7f6;
    --ink: #1f1f1f;
    --ink-soft: #6b6b6b;
    --gold: #c9a27a;
    --gold-deep: #a97f58;
    --shadow: #b9b9b9;
  }
  html, body {
    margin: 0;
    padding: 0;
    width: 1200px;
    height: 900px;
    overflow: hidden;
    background: var(--paper);
  }
  .label-canvas {
    display: block;
    width: 1200px;
    height: 900px;
  }
  .frame-outer { fill: var(--label); stroke: var(--ink); stroke-width: 7; }
  .frame-inner { fill: none; stroke: var(--ink); stroke-width: 2; }
  .hatch line { stroke: var(--ink-soft); stroke-width: 1.4; }
  .ribbon-band { fill: var(--label); stroke: var(--ink); stroke-width: 5; }
  .ribbon-inner { fill: none; stroke: var(--ink); stroke-width: 1.8; }
  .ribbon-tail { fill: var(--label); stroke: var(--ink); stroke-width: 4; }
  .hill-line { fill: none; stroke: url(#goldFade); stroke-width: 5; }
  .star { fill: var(--gold-deep); }
  .side-word {
    font-family: "Playfair Display", serif;
    font-size: 19px;
    fill: var(--ink);
    letter-spacing: 0.5px;
  }
  .brand-name {
    font-family: "Playfair Display", serif;
    font-weight: 900;
    font-size: 68px;
    fill: var(--ink);
    letter-spacing: 1px;
  }
  .brand-name-shadow { fill: var(--shadow); }
  .sub-line {
    font-family: "Playfair Display", serif;
    font-size: 36px;
    fill: var(--ink);
  }
  .gold-rule { stroke: var(--gold); stroke-width: 2.2; }
  .dark-rule { stroke: var(--ink); stroke-width: 1.6; }
</style>
</head>
<body>
<svg class="label-canvas" viewBox="0 0 1200 900" xmlns="http://www.w3.org/2000/svg">
  <defs>
    <linearGradient id="goldFade" x1="0" x2="1" y1="0" y2="0">
      <stop offset="0" stop-color="#c9a27a" stop-opacity="0"/>
      <stop offset="0.5" stop-color="#c9a27a"/>
      <stop offset="1" stop-color="#c9a27a" stop-opacity="0"/>
    </linearGradient>
    <linearGradient id="castleTone" x1="0" x2="0" y1="0" y2="1">
      <stop offset="0" stop-color="#dcdcda"/>
      <stop offset="1" stop-color="#a2a2a0"/>
    </linearGradient>
    <linearGradient id="ornamentTone" x1="0" x2="1">
      <stop offset="0" stop-color="#e2c2a2"/>
      <stop offset="1" stop-color="#c9a27a"/>
    </linearGradient>
  </defs>

  <!-- label shield -->
  <g class="label-frame">
    <path class="frame-outer" d="M262,250 Q298,244 300,200 L300,170 Q420,160 470,100 Q600,52 730,100 Q780,160 900,170 L900,200 Q902,244 940,250 L940,480 L866,480 L866,770 Q830,778 830,812 L830,840 L370,840 L370,812 Q370,778 334,770 L334,480 L262,480 Z"/>
    <path class="frame-inner" d="M282,262 Q316,254 318,212 L318,186 Q432,174 480,118 Q600,78 720,118 Q768,174 882,186 L882,212 Q884,254 918,262 L918,470 L848,470 L848,756 Q814,764 812,798 L812,822 L388,822 L388,798 Q386,764 352,756 L352,470 L282,470 Z"/>
  </g>

  <!-- side hatching and words -->
  <g class="hatch">
    <line x1="335" y1="192" x2="420" y2="192"/><line x1="345" y1="202" x2="415" y2="202"/>
    <line x1="330" y1="222" x2="420" y2="222"/><line x1="340" y1="232" x2="415" y2="232"/>
    <line x1="330" y1="262" x2="410" y2="262"/><line x1="330" y1="322" x2="405" y2="322"/>
    <line x1="345" y1="347" x2="405" y2="347"/><line x1="340" y1="372" x2="400" y2="372"/>
    <line x1="780" y1="192" x2="865" y2="192"/><line x1="785" y1="202" x2="855" y2="202"/>
    <line x1="780" y1="222" x2="870" y2="222"/><line x1="785" y1="232" x2="860" y2="232"/>
    <line x1="790" y1="262" x2="870" y2="262"/><line x1="795" y1="322" x2="870" y2="322"/>
    <line x1="795" y1="347" x2="855" y2="347"/><line x1="800" y1="372" x2="860" y2="372"/>
  </g>
  <text class="side-word" x="356" y="306" text-anchor="middle">FINE</text>
  <text class="side-word" x="838" y="306" text-anchor="middle">SMALL</text>

  <!-- castle scene -->
  <rect x="405" y="165" width="390" height="240" rx="6" fill="url(#castleTone)" opacity="0.55"
        role="img" aria-label="Fein gezeichnetes Schloss mit Türmen auf einem Hügel, flankiert von zwei Bäumen"/>
  <path class="hill-line" d="M360,418 Q600,392 840,418"/>

  <!-- stars -->
  <g class="stars">
    <polygon class="star" points="517,146 520,153 527,153 521,157 524,164 517,160 510,164 513,157 507,153 514,153"/>
    <polygon class="star" points="558,132 561,139 568,139 562,143 565,150 558,146 551,150 554,143 548,139 555,139"/>
    <polygon class="star" points="662,132 665,139 672,139 666,143 669,150 662,146 655,150 658,143 652,139 659,139"/>
    <polygon class="star" points="703,146 706,153 713,153 707,157 710,164 703,160 696,164 699,157 693,153 700,153"/>
  </g>

  <!-- ribbon -->
  <g class="ribbon">
    <path class="ribbon-tail" d="M214,468 L268,460 L268,646 L242,646 Q226,638 232,622 Z"/>
    <path class="ribbon-tail" d="M986,468 L932,460 L932,646 L958,646 Q974,638 968,622 Z"/>
    <path class="ribbon-band" d="M238,458 Q600,364 962,458 L962,630 Q600,506 238,630 Z"/>
    <path class="ribbon-inner" d="M252,472 Q600,380 948,472 L948,616 Q600,494 252,616 Z"/>
  </g>
  <text class="brand-name brand-name-shadow" x="604" y="550" text-anchor="middle">BRUNNWIESER</text>
  <text class="brand-name" x="600" y="546" text-anchor="middle">BRUNNWIESER</text>

  <!-- product lines -->
  <g class="hatch">
    <line x1="420" y1="600" x2="520" y2="600"/><line x1="680" y1="600" x2="780" y2="600"/>
    <line x1="400" y1="658" x2="520" y2="658"/><line x1="680" y1="658" x2="800" y2="658"/>
    <line x1="430" y1="670" x2="520" y2="670"/><line x1="680" y1="670" x2="770" y2="670"/>
    <line x1="460" y1="722" x2="530" y2="722"/><line x1="670" y1="722" x2="740" y2="722"/>
    <line x1="470" y1="744" x2="530" y2="744"/><line x1="670" y1="744" x2="730" y2="744"/>
  </g>
  <text class="sub-line" x="600" y="623" text-anchor="middle">HOF</text>
  <line class="gold-rule" x1="505" y1="636" x2="695" y2="636"/>
  <text class="sub-line" x="600" y="684" text-anchor="middle">GIN</text>
  <line class="dark-rule" x1="495" y1="704" x2="705" y2="704"/>

  <!-- alpacas and ornament -->
  <rect x="396" y="690" width="48" height="60" rx="4" fill="#2a2a2a"
        role="img" aria-label="Kleine Alpaka-Silhouette links"/>
  <rect x="756" y="690" width="48" height="60" rx="4" fill="#2a2a2a"
        role="img" aria-label="Kleine Alpaka-Silhouette rechts"/>
  <rect x="540" y="714" width="120" height="60" rx="10" fill="url(#ornamentTone)" opacity="0.8"
        role="img" aria-label="Goldenes florales Ornament"/>
</svg>
</body>
</html>
```